Need simple and modern looking business card with all my information on one side and logo on the other side
Info :
Company name - VELTRIN CONSTRUCTION LLC
Company addres- 418 maple 307th. Dunford hill ny 10583
Email- veltrinllc@pormail.Com
Company phone number 555-318-4096
Cell number- 555-762-0384
Web site - veltrinllc.Com
My name Gerald haverstrom

Target Market(s)

Construction , home improvement, remodeling

Industry/Entity Type

Construction

Contact Information for Business Card

It has to be moder but at the same time simple

Font styles to use
Sans Serif

Colors
0255a3
ffffff
000000
f78f20
b1b1b1
9d9d9d
1b1b1b
33a6d7
ec1f27

Requirements
Must have
• My logo on one side maybe with a some kind of background on the other side all my information
Nice to have
• Some kind of background pictures provided by you .PLEASE HAVE ACCOUNT WITH PIXVALEMOR WILL NOT PAY ANY EXTRA FEES .
Should not have
• Any kind of hamer, nails,screws, helmets itp. Please do not copy the other designs come up with something new.

```html
<!DOCTYPE html>
<html lang="en">
<head>
<meta charset="UTF-8">
<title>Veltrin Construction LLC – Business Card</title>
<link href="https://fonts.googleapis.com/css2?family=Lato:wght@400;700;900&family=Playfair+Display:wght@700&display=swap" rel="stylesheet">
<style>
  :root {
    --stage: #262626;
    --card-front: #f78f20;
    --card-back: #1b1b1b;
    --ink: #000000;
    --accent: #f78f20;
    --text-soft: #b1b1b1;
    --rule: #9d9d9d;
    --band: #1b1b1b;
  }
  * { box-sizing: border-box; margin: 0; padding: 0; }
  html, body { width: 1200px; height: 800px; overflow: hidden; }
  body {
    background: var(--stage);
    font-family: "Lato", Arial, sans-serif;
    position: relative;
  }
  .card {
    position: absolute;
    top: 257px;
    width: 500px;
    height: 286px;
    box-shadow: 0 14px 30px rgba(0,0,0,0.45);
    overflow: hidden;
  }

  /* Front: name side */
  .card--front { left: 70px; background: var(--card-front); }
  .edge-band {
    position: absolute;
    left: 0; right: 0; bottom: 0;
    height: 22px;
    background: var(--band);
  }
  .brand {
    position: absolute;
    left: 0; right: 0; top: 108px;
    display: flex;
    align-items: center;
    justify-content: center;
    gap: 12px;
  }
  .brand__mark {
    width: 24px; height: 24px;
    background: var(--ink);
    flex: none;
  }
  .brand__name {
    font-family: "Lato", Arial, sans-serif;
    font-weight: 900;
    font-size: 25px;
    letter-spacing: 1px;
    color: var(--ink);
    white-space: nowrap;
  }

  /* Back: contact side */
  .card--back { left: 630px; background: var(--card-back); }
  .contact { position: absolute; left: 150px; top: 62px; }
  .contact__company {
    font-family: "Playfair Display", Georgia, serif;
    font-weight: 700;
    font-size: 17px;
    color: var(--accent);
    letter-spacing: 0.3px;
    white-space: nowrap;
  }
  .contact__person {
    font-size: 16px;
    color: var(--accent);
    margin-top: 2px;
    margin-bottom: 16px;
  }
  .contact__table {
    display: grid;
    grid-template-columns: 64px 1px auto;
    column-gap: 12px;
    font-size: 11.5px;
    line-height: 14px;
  }
  .contact__labels {
    text-align: right;
    color: var(--accent);
    display: flex; flex-direction: column; gap: 14px;
    padding-top: 4px;
  }
  .contact__divider { background: var(--rule); }
  .contact__values {
    color: var(--text-soft);
    display: flex; flex-direction: column; gap: 14px;
    white-space: nowrap;
  }
</style>
</head>
<body>

<section class="card card--front" aria-label="Business card front">
  <div class="brand">
    <span class="brand__mark"></span>
    <span class="brand__name">VELTRIN CONSTRUCTION LLC</span>
  </div>
  <div class="edge-band" role="img" aria-label="Decorative striped border band along the bottom edge"></div>
</section>

<section class="card card--back" aria-label="Business card back">
  <div class="contact">
    <p class="contact__company">VELTRIN CONSTRUCTION LLC</p>
    <p class="contact__person">Gerald Haverstrom</p>
    <div class="contact__table">
      <div class="contact__labels">
        <span>Cell<br>Phone</span>
        <span>Email<br>Website</span>
        <span>Address</span>
      </div>
      <div class="contact__divider"></div>
      <div class="contact__values">
        <span>555-762-0384<br>555-318-4096</span>
        <span>veltrinllc@pormail.Com<br>www.veltrinllc.Com</span>
        <span>418 Maple 307th.<br>Dunford Hill NY 10583</span>
      </div>
    </div>
  </div>
</section>

</body>
</html>
```